Professional Modern Website Design

We are a premium IT services provider to the financial industry based in London. Our company is called Veltra our current holding page is www.veltra-example.co.uk. We require a new website to match our new corporate identity. This project is for the design phase only. Development will be handled in-house. I have attached examples of wire frames we have developed (although open to suggestions for improvement) Our brand document that should demonstrate current brand, inc how we communicate to potential clients and finally mostly completed web-content.
We are looking for designers that can create something that sets us apart from our competitors.
Target Market(s)
IT Decision makers in Finance companies such as; hedge funds, private investment banks etc
Industry/Entity Type
Financial
Number of Pages Required
5+ page
Requirements
Must have
- hexagon elements in the design, unique design.
Nice to have
- Blog and social media feeds
Should not have
- Should not resemble a downloaded template

```html
<!DOCTYPE html>
<html lang="en">
<head>
<meta charset="utf-8">
<title>Veltra — Systems Integration for Finance</title>
<link href="https://fonts.googleapis.com/css2?family=Roboto+Condensed:wght@300;400;700&display=swap" rel="stylesheet">
<style>
:root{
  --orange:#ef6c22;
  --orange-light:#f58a3c;
  --ink:#1d1d1d;
  --text:#333333;
  --white:#ffffff;
  --footer:#252525;
  --footer-deep:#1a1a1a;
  --muted:#777777;
  --photo-a:#cfcfcf;
  --photo-b:#8d8d8d;
}
*{margin:0;padding:0;box-sizing:border-box}
html,body{width:1200px;height:2550px;overflow:hidden;background:var(--white)}
body{position:relative;font-family:"Roboto Condensed",Arial,sans-serif;color:var(--text)}
.abs{position:absolute}

/* Hero */
.hero{position:absolute;left:0;top:0;width:1200px;height:733px;
  background:linear-gradient(100deg,#050505 0%,#2a1a10 30%,#9a4c1c 60%,#e07a2c 85%,#f39a4a 100%)}
.brand{position:absolute;left:96px;top:40px;display:flex;flex-direction:column;align-items:center;gap:12px}
.brand-mark{width:70px;height:70px;background:var(--orange)}
.brand-name{color:#d8d8d8;font-size:18px;letter-spacing:6px}
.nav{position:absolute;top:58px;left:0;width:1200px;height:40px}
.nav a{position:absolute;color:var(--white);text-decoration:none;font-size:23px}
.nav a.dark{color:#1b1b1b}
.nav-active-bar{position:absolute;left:517px;top:0;width:95px;height:5px;background:var(--white)}
.hero-title{position:absolute;top:228px;left:0;width:1200px;text-align:center;color:var(--white);font-weight:300;font-size:50px}
.hero-lead{position:absolute;top:330px;left:150px;width:900px;text-align:center;color:var(--white);font-weight:300;font-size:25px;line-height:36px}
.hero-button{position:absolute;left:512px;top:462px;width:177px;height:51px;background:var(--orange);color:var(--white);font-size:22px;display:flex;align-items:center;justify-content:center;box-shadow:0 4px 0 #b84e12}
.slider-dots{position:absolute;top:689px;left:548px;display:flex;gap:20px}
.slider-dots span{width:21px;height:21px;border-radius:50%;border:2px solid var(--white)}
.slider-dots span.active{background:var(--white)}

/* Who are you */
.network{position:absolute;left:0;top:0}
.who-title{position:absolute;left:509px;top:836px;width:180px;text-align:center;color:var(--white);font-size:40px;line-height:50px;font-weight:300}
.who-intro{position:absolute;left:300px;top:1015px;width:600px;text-align:center;font-size:16px;line-height:22px;color:#111}
.role-title{position:absolute;color:var(--orange);font-size:21px}
.role-text{position:absolute;font-size:16px;line-height:22.7px;color:var(--text);letter-spacing:.1px}

/* Footer */
.footer{position:absolute;left:0;top:2190px;width:1200px;height:318px;background:linear-gradient(120deg,#2b2b2b,#1f1f1f 50%,#2a2a2a)}
.footer-bar{position:absolute;left:0;top:2508px;width:1200px;height:42px;background:var(--footer-deep);color:var(--white);font-size:16px;display:flex;align-items:center;justify-content:center}
.footer-bar b{color:var(--orange);font-weight:700}
.footer-heading{position:absolute;color:var(--orange);font-size:31px;font-weight:400}
.news-item{position:absolute;left:80px;width:298px}
.news-title{color:var(--white);font-size:16px;line-height:20px}
.news-date{color:#6d6d6d;font-size:13px;margin-top:3px}
.news-rule{position:absolute;left:80px;width:298px;border-top:1px dashed #8a8a8a}
.tweet{position:absolute;left:444px;display:flex;gap:12px}
.tweet-avatar{width:56px;height:56px;background:#111;border:1px solid #444;display:flex;align-items:center;justify-content:center}
.tweet-avatar span{width:30px;height:30px;background:var(--orange)}
.tweet-body{font-size:14px;line-height:19px;color:var(--white)}
.tweet-handle{color:var(--orange)}
.tweet-link{color:#8a8a8a}
.contact-label{position:absolute;left:811px;color:var(--orange);font-size:22px}
.contact-number{position:absolute;left:838px;color:var(--white);font-size:16px}
</style>
</head>
<body>

<header class="hero" role="img" aria-label="Photograph of glowing light bulbs lying in a row, washed in orange light"></header>
<div class="brand"><span class="brand-mark"></span><span class="brand-name">VELTRA</span></div>
<nav class="nav">
  <span class="nav-active-bar"></span>
  <a style="left:541px;top:0">About</a>
  <a class="dark" style="left:655px;top:0">Services</a>
  <a class="dark" style="left:791px;top:0">Partners</a>
  <a class="dark" style="left:927px;top:0">Clients</a>
  <a class="dark" style="left:1048px;top:0">Contact</a>
</nav>
<h1 class="hero-title">You need integration. We’re always there with you.</h1>
<p class="hero-lead">Veltra is one of the leading systems integrators to the world’s finance sector. We are an extension of your business and our services portfolio has been built so you always have access to a complete partner.</p>
<a class="hero-button">READ MORE</a>
<div class="slider-dots"><span class="active"></span><span></span><span></span></div>

<svg class="network" width="1200" height="2190" viewBox="0 0 1200 2190">
  <defs>
    <linearGradient id="photo-fill" x1="0" y1="0" x2="0" y2="1">
      <stop offset="0" stop-color="var(--photo-a)"/>
      <stop offset="1" stop-color="var(--photo-b)"/>
    </linearGradient>
  </defs>
  <g fill="none" stroke="#ef6c22" stroke-width="3">
    <polyline points="490,884 48,1037 48,2074 598,2137 1154,2074 1154,1037 709,887"/>
    <line x1="490" y1="884" x2="502" y2="882"/>
    <line x1="709" y1="887" x2="696" y2="884"/>
    <line x1="48" y1="1256" x2="433" y2="1190"/>
    <line x1="769" y1="1433" x2="1154" y2="1547"/>
    <line x1="48" y1="1624" x2="433" y2="1716"/>
    <line x1="771" y1="1985" x2="1154" y2="1850"/>
    <polyline points="575,1259 595,1309 616,1343"/>
    <polyline points="610,1524 592,1559 575,1588"/>
    <polyline points="575,1790 592,1836 610,1905"/>
    <line x1="640" y1="2075" x2="598" y2="2137"/>
  </g>
  <g fill="#ef6c22">
    <circle cx="490" cy="884" r="7"/><circle cx="709" cy="887" r="7"/>
    <circle cx="48" cy="1037" r="7"/><circle cx="1154" cy="1037" r="7"/>
    <circle cx="48" cy="1256" r="7"/><circle cx="48" cy="1624" r="7"/>
    <circle cx="1154" cy="1547" r="7"/><circle cx="1154" cy="1850" r="7"/>
    <circle cx="598" cy="2137" r="7"/>
    <circle cx="595" cy="1309" r="7"/><circle cx="592" cy="1559" r="7"/><circle cx="592" cy="1836" r="7"/>
  </g>
  <polygon points="599,782 696,838 696,950 599,1006 502,950 502,838" fill="#fff" stroke="#ef6c22" stroke-width="3"/>
  <polygon points="599,790 689,842 689,946 599,998 509,946 509,842" fill="#ef6c22"/>

  <polygon points="527,1070 621,1124 621,1232 527,1286 433,1232 433,1124" fill="#fff" stroke="#ef6c22" stroke-width="3"/>
  <polygon role="img" aria-label="Portrait of a smiling businessman in a grey suit" points="527,1080 612,1129 612,1227 527,1276 442,1227 442,1129" fill="url(#photo-fill)"/>
  <polygon points="675,1323 769,1377 769,1485 675,1539 581,1485 581,1377" fill="#fff" stroke="#ef6c22" stroke-width="3"/>
  <polygon role="img" aria-label="Portrait of a smiling businesswoman" points="675,1333 760,1382 760,1480 675,1529 590,1480 590,1382" fill="url(#photo-fill)"/>
  <polygon points="527,1601 621,1655 621,1763 527,1817 433,1763 433,1655" fill="#fff" stroke="#ef6c22" stroke-width="3"/>
  <polygon role="img" aria-label="Portrait of a young man in a suit" points="527,1611 612,1660 612,1758 527,1807 442,1758 442,1660" fill="url(#photo-fill)"/>
  <polygon points="677,1881 771,1935 771,2043 677,2097 583,2043 583,1935" fill="#fff" stroke="#ef6c22" stroke-width="3"/>
  <polygon role="img" aria-label="Photograph of office employees reviewing documents at a desk" points="677,1891 762,1940 762,2038 677,2087 592,2038 592,1940" fill="url(#photo-fill)"/>
</svg>

<h2 class="who-title">Who Are<br>You?</h2>
<p class="who-intro">If you’re part of a financial organisation, we have the power to help everyone work more efficiently, productively and profitably.</p>

<h3 class="role-title" style="left:641px;top:1076px">Senior Hedge Fund Manager/CEO</h3>
<p class="role-text" style="left:641px;top:1124px;width:485px">You need to develop and implement strategies for business growth, while ensuring profitability. You’re aware your biggest asset is your staff and a happy workforce is a productive one. Security is a key concern in a changing always-on world and you need to be compliant, but you don’t want to overspend. Veltra can help you find the best solutions to help your business grow at the speed you want it to.</p>

<h3 class="role-title" style="left:80px;top:1326px">CFO</h3>
<p class="role-text" style="left:80px;top:1372px;width:472px">Your key responsibility is to obtain the maximum ROI from products and services. You understand investment opportunities, providing they return higher efficiencies and revenues. You are concerned more with long-term spending versus short-term and how you can get the most value out of a proposition. Veltra can advise how to boost ROI by streamlining your business to maximise return.</p>

<h3 class="role-title" style="left:636px;top:1618px">IT Manager/CTO</h3>
<p class="role-text" style="left:641px;top:1666px;width:485px">Integration with partners and services is your key concern. You want to make sure any IT system you implement will work with the whole infrastructure of your company. You don’t want your team to waste valuable time dealing with things that don’t matter. Veltra provides the whole picture to ensure your company is ready for the next generation of IT.</p>

<h3 class="role-title" style="left:80px;top:1889px">Employees</h3>
<p class="role-text" style="left:80px;top:1935px;width:482px">You’re working hard, but not getting anywhere fast. You want the tools to make your job easier so you can spend more time thinking about what you’re doing rather than how you’re doing it. You shouldn’t have to think about the technology you’re using, because it should just work. Veltra can help you get back on track everyday.</p>

<footer class="footer"></footer>
<h2 class="footer-heading" style="left:80px;top:2204px">Latest News</h2>
<div class="news-item" style="top:2262px"><div class="news-title">Cloud growth in the financial sector</div><div class="news-date">Friday, 6 March 2015</div></div>
<div class="news-rule" style="top:2315px"></div>
<div class="news-item" style="top:2324px"><div class="news-title">2015: Year of the cloud</div><div class="news-date">Friday, 27 February 2015</div></div>
<div class="news-rule" style="top:2377px"></div>
<div class="news-item" style="top:2386px"><div class="news-title">Airlines reach new heights with the help of Cloud Computing</div><div class="news-date">Friday, 13 February 2015</div></div>

<h2 class="footer-heading" style="left:444px;top:2204px">Latest Tweets</h2>
<div class="tweet" style="top:2261px"><div class="tweet-avatar"><span></span></div><div class="tweet-body"><div class="tweet-handle">@Veltra_</div><div>Jon Marsh spills the beans on Kestrel Pay</div><div class="tweet-link">http://lnk.example/JGeXL</div></div></div>
<div class="tweet" style="top:2332px"><div class="tweet-avatar"><span></span></div><div class="tweet-body"><div class="tweet-handle">@Veltra_</div><div>How the Orbis Studios attack changed</div><div class="tweet-link">http://lnk.example/JGeMJ</div></div></div>
<div class="tweet" style="top:2406px"><div class="tweet-avatar"><span></span></div><div class="tweet-body"><div class="tweet-handle">@Veltra_</div><div>Trust in the digital world: Is it at an all</div><div class="tweet-link">http://lnk.example/JGesQ</div></div></div>

<h2 class="footer-heading" style="left:811px;top:2204px">Contact Us</h2>
<div class="contact-label" style="top:2258px">SUPPORT:</div>
<div class="contact-number" style="top:2300px">+44 20 0000 1201</div>
<div class="contact-label" style="top:2342px">SALES:</div>
<div class="contact-number" style="top:2384px">+44 20 0000 1202</div>
<svg class="abs" style="left:810px;top:2417px" width="300" height="70" viewBox="0 0 300 70" role="img" aria-label="Social media links">
  <polygon points="37,4 66,19 66,51 37,66 8,51 8,19" fill="#ef6c22"/>
  <polygon points="110,4 139,19 139,51 110,66 81,51 81,19" fill="#fff"/>
  <polygon points="183,4 212,19 212,51 183,66 154,51 154,19" fill="#fff"/>
  <polygon points="256,4 285,19 285,51 256,66 227,51 227,19" fill="#fff"/>
</svg>

<div class="footer-bar">©&nbsp;<b>Veltra</b>&nbsp;- 2015. All Rights Reserved.</div>
</body>
</html>
```